Swim School Certificates

We are looking to have some certificates designed for our Learn to Swim School. These will be handed out to our students when they complete each level. We will need different certificates for each level, however, we would like a consistent theme throughout, so each level may only have a slight variation. We are happy for you to just show us a couple of variations to begin with, so we can see how these would work. Then once we decide on the winning design, you can complete the rest.
The levels are:
Bubs 1
Bubs 2
Toddler 1
Toddler 2
Beginner 1
Beginner 2
Beginner 3
Stroke Development 1
Stroke Development 2
Advanced 1
Advanced 2
Squad
The Certificates should include:
Congratulations to:
(blank line for name)
You have completed (level name), Keep up the good work!!!
Signed: (blank line) Date: (blank line)
I've included a copy of our logo, and a copy of our governing bodies logo both of which should be included on the certificate.
I've also included some examples of certificates we like, to give you an idea of our style. We are happy for the bubs and toddler certificates to be more child focused, so they can included a kid friendly element to them, however this will need to reduce to a more simplistic design as the levels increase into beginner and stroke etc.
You can also look on our Facebook page to get an idea of what we do.
https://www.facebook.com/coralridgeswimschool/?ref=bookmarks
We will also need editable source files upon completion as we may be looking to change the name of some classes in the future.
Please let us know if you need any of the files in other formats
Kind Regards
Maree

```html
<!DOCTYPE html>
<html lang="en">
<head>
<meta charset="utf-8">
<title>Coral Ridge Swim School – Level Certificate</title>
<link rel="stylesheet" href="https://fonts.googleapis.com/css2?family=Marcellus&family=Indie+Flower&family=Arimo:wght@400;700&display=swap">
<style>
  :root {
    --sky-blue: #4283c8;
    --deep-blue: #2c3f94;
    --navy-wave: #27286a;
    --mid-wave: #2d62ae;
    --bright-wave: #3c86cb;
    --shallow-wave: #6cc2e2;
    --paper-white: #ffffff;
    --badge-ring: #1aa3d9;
  }
  html, body {
    margin: 0;
    padding: 0;
    overflow: hidden;
    background: #ffffff;
  }
  .certificate {
    position: relative;
    width: 1200px;
    height: 927px;
    overflow: hidden;
    background: linear-gradient(90deg, var(--sky-blue) 0%, #3a6cb8 50%, var(--deep-blue) 100%);
    color: var(--paper-white);
  }
  .certificate__waves {
    position: absolute;
    inset: 0;
    width: 1200px;
    height: 927px;
  }
  .certificate__title {
    position: absolute;
    left: 0;
    width: 1260px;
    top: 40px;
    margin: 0;
    text-align: center;
    font-family: "Marcellus", serif;
    font-weight: 400;
    font-size: 112px;
    letter-spacing: 4px;
    -webkit-text-stroke: 1.5px var(--paper-white);
  }
  .fill-line {
    position: absolute;
    text-align: center;
    font-family: "Arimo", sans-serif;
    font-size: 29px;
    border-bottom: 4px solid var(--paper-white);
    padding-bottom: 10px;
  }
  .fill-line--name { left: 235px; width: 705px; top: 194px; }
  .fill-line--level { left: 262px; width: 705px; top: 392px; }
  .script {
    position: absolute;
    left: 0;
    width: 1200px;
    margin: 0;
    text-align: center;
    font-family: "Indie Flower", cursive;
    font-weight: 400;
  }
  .script--completed { top: 288px; font-size: 66px; letter-spacing: 3px; }
  .script--encourage { top: 484px; font-size: 56px; letter-spacing: 4px; left: 0; width: 1200px; }
  .sign-field {
    position: absolute;
    top: 616px;
    display: flex;
    align-items: flex-end;
    font-family: "Indie Flower", cursive;
    font-size: 31px;
  }
  .sign-field__line {
    display: inline-block;
    height: 0;
    border-bottom: 2px solid var(--paper-white);
    margin-left: 10px;
    margin-bottom: 12px;
  }
  .sign-field--signed { left: 184px; }
  .sign-field--signed .sign-field__line { width: 207px; }
  .sign-field--date { left: 775px; }
  .sign-field--date .sign-field__line { width: 152px; }
  .school-name {
    position: absolute;
    left: 56px;
    top: 740px;
    width: 242px;
    margin: 0;
    text-align: center;
    font-family: "Arimo", sans-serif;
    font-weight: 700;
    font-size: 38px;
    line-height: 1.15;
    color: var(--paper-white);
  }
  .partner-badge {
    position: absolute;
    left: 967px;
    top: 697px;
    width: 180px;
    height: 180px;
  }
</style>
</head>
<body>
  <main class="certificate">
    <svg class="certificate__waves" viewBox="0 0 1200 927" aria-hidden="true">
      <path fill="var(--navy-wave)" d="M0,690 C200,640 420,720 640,640 C800,580 900,480 1200,468 L1200,927 L0,927 Z"/>
      <path fill="var(--mid-wave)" d="M0,790 C220,740 420,800 620,720 C820,640 960,560 1200,600 L1200,927 L0,927 Z"/>
      <path fill="var(--bright-wave)" d="M0,870 C250,820 450,900 700,800 C880,730 1000,700 1200,760 L1200,927 L0,927 Z"/>
      <path fill="var(--shallow-wave)" d="M300,927 C500,880 700,900 850,800 C950,740 1080,760 1200,820 L1200,927 Z"/>
    </svg>

    <h1 class="certificate__title">Congratulation!</h1>

    <div class="fill-line fill-line--name">text here</div>
    <p class="script script--completed">you have completed</p>
    <div class="fill-line fill-line--level">text here</div>
    <p class="script script--encourage">Keep up the good work</p>

    <div class="sign-field sign-field--signed">Signed<span class="sign-field__line"></span></div>
    <div class="sign-field sign-field--date">Date<span class="sign-field__line"></span></div>

    <p class="school-name">Coral Ridge<br>Swim School</p>

    <svg class="partner-badge" viewBox="0 0 180 180" role="img" aria-label="Governing body registration badge">
      <rect x="0" y="0" width="180" height="180" fill="var(--paper-white)"/>
      <circle cx="90" cy="90" r="72" fill="var(--badge-ring)"/>
    </svg>
  </main>
</body>
</html>
```